Business Card Design Project : Ferncliff Media

In preparation for market launch, Whistler's Ferncliff Media require the development of a business card. Ferncliff Media is a Community online publishing web portal. We provide the the city of Whistler located in B.C. (Canada) business directories, News, Classified ads, News, Events and blogs etc.

The main focus of the brand is to help local businesses to corporate with their online advertisement and marketing. Meeting our clients face to face is a must (B2B).

Target Market(s)

The target market is B2B customers. Business Owners to Marketing, advertising Managers

Industry/Entity Type

Business

Requirements
Must have
• - The business card will be two sided.
the BACK side will have our logo which consist of (icon, url,slogan) submited. The logo will be middle and centred.

The FRONT side should have company details:

Company Legal Name: TALLPINE FERNCLIFF MEDIA

Dale Morrow
Director of Sales & Marketing

www.tallpineferncliff.biz
dale@tallpineferncliff.biz

Phone: 604 555 0138
#2217 - 581 E. Harlow Ave.
Vancouver, B.C. V6N2K4 Canada
Nice to have
• - For the "FRONT" side of our business card. You can separate or re-arrange with our logo components (icon, logo,slogan). It does not have to be together.

Also our company legal name is rather long so arrange or organize the name in a way to make it shorter. Your experience and creativity will have to come in play.
Should not have
• should not have other colors beside logo color and black text (2 colors). Also nothing Three dimensional

```html
<!DOCTYPE html>
<html lang="en">
<head>
<meta charset="utf-8">
<title>Ferncliff Media — Business Card</title>
<link rel="stylesheet" href="https://fonts.googleapis.com/css2?family=Open+Sans:wght@400;600;700&display=swap">
<style>
  :root {
    --brand-blue: #1679c0;
    --brand-blue-deep: #0d5c9c;
    --brand-blue-light: #2a90d6;
    --ink: #1c1c1c;
    --paper: #ffffff;
    --mist: #e6e8ea;
    --backdrop: #d9dcdf;
  }
  * { box-sizing: border-box; margin: 0; padding: 0; }
  html, body { width: 1200px; height: 944px; overflow: hidden; }
  body {
    background: var(--backdrop);
    font-family: "Open Sans", Arial, sans-serif;
    position: relative;
  }
  .card {
    position: absolute;
    width: 760px;
    height: 434px;
    border-radius: 28px;
    overflow: hidden;
  }

  /* Back side */
  .card-back {
    left: 60px;
    top: 40px;
    background: radial-gradient(ellipse at 45% 40%, var(--brand-blue-light) 0%, var(--brand-blue) 55%, var(--brand-blue-deep) 100%);
  }
  .back-lockup {
    position: absolute;
    left: 110px;
    top: 110px;
  }
  .brand-name {
    display: flex;
    align-items: center;
    gap: 14px;
    font-weight: 700;
    font-size: 44px;
    color: var(--paper);
    letter-spacing: 0.5px;
  }
  .brand-mark {
    width: 30px;
    height: 30px;
    border-radius: 50%;
    background: currentColor;
  }
  .back-url {
    margin-top: 30px;
    font-weight: 700;
    font-size: 38px;
    color: var(--ink);
    letter-spacing: -0.5px;
  }
  .back-slogan {
    margin-left: 110px;
    font-size: 27px;
    color: var(--paper);
  }

  /* Front side */
  .card-front {
    left: 380px;
    top: 490px;
    background: var(--paper);
  }
  .front-bg { position: absolute; inset: 0; }
  .front-brand {
    position: absolute;
    left: 48px;
    top: 88px;
  }
  .front-brand .brand-name {
    font-size: 34px;
    color: var(--brand-blue);
    gap: 12px;
  }
  .front-brand .brand-mark { width: 22px; height: 22px; }
  .front-slogan {
    margin-top: 22px;
    font-size: 20px;
    color: var(--ink);
  }
  .contact {
    position: absolute;
    left: 408px;
    top: 52px;
    color: var(--ink);
  }
  .person-name { font-weight: 700; font-size: 22px; letter-spacing: 0.5px; }
  .person-title { font-size: 14px; color: var(--brand-blue); margin-top: 4px; }
  .details { list-style: none; margin-top: 34px; font-size: 15px; line-height: 1.3; }
  .details li { display: flex; gap: 8px; margin-bottom: 4px; }
  .details svg { flex: 0 0 auto; width: 16px; height: 16px; margin-top: 2px; fill: var(--brand-blue-deep); }
  .front-url {
    position: absolute;
    left: 0;
    right: 0;
    bottom: 30px;
    text-align: center;
    font-size: 30px;
    font-weight: 600;
    letter-spacing: 2px;
    color: var(--paper);
  }
</style>
</head>
<body>

  <section class="card card-back" aria-label="Card back">
    <div class="back-lockup">
      <div class="brand-name"><span class="brand-mark"></span>Ferncliff Media</div>
      <p class="back-url">www.tallpineferncliff.biz</p>
      <p class="back-slogan">Your information gateway</p>
    </div>
  </section>

  <section class="card card-front" aria-label="Card front">
    <svg class="front-bg" viewBox="0 0 760 434" preserveAspectRatio="none" aria-hidden="true">
      <defs>
        <linearGradient id="mistFade" x1="0" y1="0" x2="0" y2="1">
          <stop offset="0" stop-color="#ffffff"/>
          <stop offset="1" stop-color="#dfe2e5"/>
        </linearGradient>
        <linearGradient id="bandBlue" x1="0" y1="0" x2="0" y2="1">
          <stop offset="0" stop-color="#2a90d6"/>
          <stop offset="1" stop-color="#0d5c9c"/>
        </linearGradient>
      </defs>
      <path d="M0,200 C260,240 520,290 760,300 L760,434 L0,434 Z" fill="url(#mistFade)"/>
      <path d="M0,262 C250,292 500,330 760,334" fill="none" stroke="#1c1c1c" stroke-width="9"/>
      <path d="M0,300 C260,330 500,360 760,352 L760,434 L0,434 Z" fill="url(#bandBlue)"/>
    </svg>

    <div class="front-brand">
      <div class="brand-name"><span class="brand-mark"></span>Ferncliff Media</div>
      <p class="front-slogan">Your information gateway</p>
    </div>

    <div class="contact">
      <p class="person-name">Dale Morrow</p>
      <p class="person-title">Director of Sales &amp; Marketing</p>
      <ul class="details">
        <li>
          <svg viewBox="0 0 16 16"><path d="M8 1 1 7.5h2V15h4v-4h2v4h4V7.5h2z"/></svg>
          <span>#2217 - 581 E. Harlow Ave.<br>Vancouver, B.C. V6N2K4 Canada</span>
        </li>
        <li>
          <svg viewBox="0 0 16 16"><path d="M4 1h3l1 4-2 1.5a9 9 0 0 0 3.5 3.5L11 8l4 1v3c0 1.5-1 3-3 3C6 15 1 10 1 4c0-2 1.5-3 3-3z"/></svg>
          <span>604 555 0138</span>
        </li>
        <li>
          <svg viewBox="0 0 16 16"><path d="M1 3h14v10H1z M1 3l7 6 7-6" fill="none" stroke="#0d5c9c" stroke-width="1.6"/></svg>
          <span>dale@tallpineferncliff.biz</span>
        </li>
      </ul>
    </div>

    <p class="front-url">www.tallpineferncliff.biz</p>
  </section>

</body>
</html>
```